Memorial page to show case the life and works of an individual who has passed

I would like to design a website as a memorial page for my mother. She was a very senior member of the London community and would like to design something that has a page for her biography. Gallery. Testimonials. Etc. Something that is smart and modern.
similar to
http://www.kelwynradeoffice.org/
Not to have things that are flowery it need to be a website that is smart clean and proffesional to showcase the life and works of an indiviudal

there wont be a logo as it is not a company

Industry/Entity Type

Community

Number of Pages Required

4 page

Colors
9bcb3c
abd036
ffffff
f78f20
3176b5

Requirements
Must have
• Gallary
• moving gallary at the top
• About
• Testimonials
• Videos
• Leave a message

```html
<!DOCTYPE html>
<html lang="en">
<head>
<meta charset="utf-8">
<title>Halden Memorial</title>
<link rel="stylesheet" href="https://fonts.googleapis.com/css2?family=Raleway:wght@400;500;600;700&family=Open+Sans:wght@400;600&display=swap">
<style>
:root{
  --blue:#3176b5;
  --blue-dark:#2766a3;
  --green:#9bcb3c;
  --orange:#f78f20;
  --ink:#333333;
  --body:#666666;
  --rule:#e6e6e6;
  --footer:#333333;
  --white:#ffffff;
}
*{box-sizing:border-box;margin:0;padding:0}
html,body{width:799px;height:1200px;overflow:hidden;background:var(--white)}
body{position:relative;font-family:"Open Sans",Arial,sans-serif;color:var(--body)}
.abs{position:absolute}
.site-header{top:0;left:0;width:799px;height:70px}
.brand{left:65px;top:20px;font-family:"Raleway",Arial,sans-serif;font-weight:600;font-size:22px;color:var(--blue);letter-spacing:-.3px}
.contact{left:585px;top:22px;display:flex;align-items:center;gap:8px}
.contact-icon{width:23px;height:23px;border:1.5px solid var(--green);border-radius:50%;display:flex;align-items:center;justify-content:center}
.contact-text{font-size:10px;line-height:14px;color:#555}
.main-nav{top:70px;left:0;width:799px;height:34px;background:linear-gradient(#3b83c4,var(--blue-dark))}
.main-nav ul{list-style:none;display:flex;position:absolute;left:65px;top:0;height:34px}
.main-nav li{font-size:9.5px;color:var(--white);height:34px;line-height:34px;padding:0 17px;border-right:1px solid rgba(255,255,255,.18);text-transform:uppercase}
.main-nav li.active{background:var(--green);border:0}
.main-nav li:last-child{border:0}
.hero{top:104px;left:0;width:799px;height:323px;background:linear-gradient(180deg,#d9dcde 0%,#e9eaea 38%,#c9b496 62%,#a8875c 100%)}
.hero-portrait{position:absolute;left:465px;top:0;width:270px;height:323px;background:linear-gradient(180deg,#cbbfb3 0%,#8a7f7a 45%,#6a5f60 100%);border-radius:120px 120px 0 0}
.hero-title{position:absolute;left:117px;top:110px;font-family:"Raleway",Arial,sans-serif}
.hero-title .big{font-size:37px;font-weight:700;color:var(--blue);letter-spacing:1px;line-height:38px}
.hero-title .sub{font-size:24px;font-weight:600;color:var(--ink);line-height:28px}
.hero-title p{font-size:8.5px;line-height:15px;color:var(--blue-dark);margin-top:8px}
.slide-arrow{position:absolute;top:133px;width:23px;height:23px;border-radius:50%;background:rgba(120,120,120,.65);display:flex;align-items:center;justify-content:center}
h2.section{font-family:"Raleway",Arial,sans-serif;font-weight:500;font-size:17px;color:var(--ink);text-transform:uppercase}
.welcome{left:65px;top:462px;width:442px}
.welcome p{font-size:7.3px;line-height:13.5px;margin-top:9px}
.welcome h2{margin-bottom:2px}
.divider{left:65px;top:599px;width:442px;height:1px;background:var(--rule)}
.news-title{left:65px;top:617px}
.news-item{left:66px;width:441px;height:106px}
.news-thumb{position:absolute;left:0;top:0;width:155px;height:106px}
.news-body{position:absolute;left:175px;top:-3px;width:266px}
.news-body h3{font-family:"Raleway",Arial,sans-serif;font-weight:500;font-size:11px;color:var(--ink)}
.meta{display:flex;align-items:center;gap:10px;font-size:7px;color:#777;margin:6px 0 8px}
.stars{color:var(--orange);font-size:7px;letter-spacing:.5px}
.stars .off{color:#c8c8c8}
.news-body p{font-size:7px;line-height:13.6px;text-align:justify}
.read-more{font-size:7.5px;color:#555;margin-top:7px;text-transform:uppercase}
.message-box{left:533px;top:471px;width:201px;height:106px;background:var(--blue);padding:13px 16px;color:var(--white)}
.message-box h3{font-family:"Raleway",Arial,sans-serif;font-weight:500;font-size:13.5px}
.message-box p{font-size:7.2px;line-height:12px;margin-top:5px}
.subscribe{display:flex;margin-top:8px}
.subscribe .field{width:136px;height:22px;background:var(--white);font-size:7px;color:#666;line-height:22px;padding-left:9px}
.subscribe .go{width:33px;height:22px;background:#3a3a3a;font-size:7.5px;line-height:22px;text-align:center}
.testi-title{left:533px;top:593px;font-size:13px!important}
.quote-card{left:533px;top:616px;width:201px;height:102px;border:1px solid #e8e8e8;box-shadow:0 1px 3px rgba(0,0,0,.06);padding:13px 15px;font-size:7px;line-height:16px;color:#555}
.quote-card .mark{color:#ccd4dc;font-family:Georgia,serif;font-size:16px;position:absolute;left:13px;top:5px}
.quote-card .text{text-indent:25px}
.quote-tail{left:674px;top:717px}
.author-photo{left:547px;top:729px;width:54px;height:54px;border-radius:50%;background:linear-gradient(#9aa6b3,#4a5563);border:2px solid #eee}
.author-name{left:611px;top:735px;font-size:8px;color:#555}
.author-name span{color:var(--blue)}
.author-rule{left:611px;top:751px;width:120px;height:1px;background:var(--rule)}
.pager{left:611px;top:762px;display:flex;gap:3px}
.pager span{width:15px;height:14px;border:1px solid #e1e1e1;display:flex;align-items:center;justify-content:center}
.side-rule{left:531px;top:799px;width:203px;height:1px;background:var(--rule)}
.gallery-title{left:531px;top:815px;font-size:13px!important}
.tile{width:97px;height:82px}
.site-footer{left:0;top:1041px;width:799px;height:159px}
.socials{left:341px;top:1113px;display:flex;gap:6px}
.socials span{width:19px;height:19px;border-radius:50%;background:var(--white)}
.foot-nav{left:0;top:1144px;width:799px;text-align:center;font-size:7.5px;color:var(--white);word-spacing:1px}
.foot-nav b{font-weight:400;margin:0 6px}
.copy{left:0;top:1162px;width:799px;text-align:center;font-size:8px;color:var(--white)}
</style>
</head>
<body>

<header class="abs site-header">
  <div class="abs brand">Halden Memorial</div>
  <div class="abs contact">
    <div class="contact-icon">
      <svg width="11" height="11" viewBox="0 0 24 24"><path fill="#9bcb3c" d="M6.6 10.8a15.1 15.1 0 0 0 6.6 6.6l2.2-2.2c.3-.3.7-.4 1-.2 1.1.4 2.3.6 3.6.6.6 0 1 .4 1 1V20c0 .6-.4 1-1 1A17 17 0 0 1 3 4c0-.6.4-1 1-1h3.5c.6 0 1 .4 1 1 0 1.3.2 2.5.6 3.6.1.3 0 .7-.2 1z"/></svg>
    </div>
    <div class="contact-text">Call Us : +1 555 - 014 - 2290<br>info@haldenmemorial.com</div>
  </div>
</header>

<nav class="abs main-nav">
  <ul>
    <li class="active">Home</li>
    <li style="padding:0 26px 0 34px">About Halden Memorial</li>
    <li style="padding:0 25px 0 17px">Biography</li>
    <li style="padding:0 20px 0 22px">Gallery</li>
    <li style="padding:0 23px 0 19px">Testimonials</li>
    <li>Contact Us</li>
  </ul>
</nav>

<section class="abs hero">
  <div class="hero-portrait" role="img" aria-label="Photo of a smiling older woman in a scarf and red sweater standing in tall dune grass"></div>
  <div class="hero-title">
    <div class="big">HALDEN</div>
    <div class="sub">Memorial</div>
    <p>Lorem ipsum dolor sit amet, consectetur adipiscing elit,<br>sed do eiusmod tempor incididunt ut labore</p>
  </div>
  <div class="slide-arrow" style="left:22px"><svg width="8" height="10" viewBox="0 0 8 10"><path d="M6 1 2 5l4 4" stroke="#fff" stroke-width="1.5" fill="none"/></svg></div>
  <div class="slide-arrow" style="left:752px"><svg width="8" height="10" viewBox="0 0 8 10"><path d="M2 1l4 4-4 4" stroke="#fff" stroke-width="1.5" fill="none"/></svg></div>
</section>

<section class="abs welcome">
  <h2 class="section">Welcome to Halden Memorial</h2>
  <p>Lorem ipsum dolor sit amet, consectetur adipiscing elit, sed do eiusmod tempor incididunt ut labore et dolore magna aliqua. Ut enim ad minim veniam, quis nostrud exercitation ullamco laboris nisi ut aliquip ex ea commodo consequat. Duis aute irure dolor in reprehenderit in voluptate velit esse cillum dolore eu fugiat nulla pariatur. Excepteur sint occaecat cupidatat non proident, sunt in culpa qui officia deserunt mollit anim id est laborum</p>
  <p>Lorem ipsum dolor sit amet, consectetur adipiscing elit, sed do eiusmod tempor incididunt ut labore et dolore magna aliqua. Ut enim ad minim veniam, quis nostrud exercitation ullamco laboris nisi ut aliquip ex ea commodo consequat.</p>
</section>
<div class="abs divider"></div>

<h2 class="abs section news-title">Latest News</h2>

<article class="abs news-item" style="top:650px">
  <div class="news-thumb" role="img" aria-label="Photo of an elderly woman smiling among autumn leaves" style="background:linear-gradient(120deg,#c8561c,#e49a4a 45%,#7a3d22)"></div>
  <div class="news-body">
    <h3>Nemo enim ipsam voluptatem</h3>
    <div class="meta"><span class="stars">★★★<span class="off">★★</span></span>
      <span><svg width="7" height="7" viewBox="0 0 8 8"><rect x="0" y="1" width="8" height="7" fill="#888"/></svg>&nbsp; April 3 , 2016</span>
      <span><svg width="8" height="7" viewBox="0 0 8 7"><path d="M0 0h8v5H3L1 7V5H0z" fill="#888"/></svg>&nbsp; 12 Comments</span></div>
    <p>Lorem ipsum dolor sit amet, consectetur adipiscing elit, sed do eiusmod tempor incididunt ut labore et dolore magna aliqua. Ut enim ad minim veniam, quis nostrud exercitation ullamco laboris nisi</p>
    <div class="read-more">Read more &#10140;</div>
  </div>
</article>

<article class="abs news-item" style="top:776px">
  <div class="news-thumb" role="img" aria-label="Photo of a smiling woman leaning on a bicycle in a park" style="background:linear-gradient(120deg,#8fb35a,#b9cfe0 50%,#6d8a4a)"></div>
  <div class="news-body">
    <h3>Nemo enim ipsam voluptatem</h3>
    <div class="meta"><span class="stars">★★★<span class="off">★★</span></span>
      <span><svg width="7" height="7" viewBox="0 0 8 8"><rect x="0" y="1" width="8" height="7" fill="#888"/></svg>&nbsp; April 3 , 2016</span>
      <span><svg width="8" height="7" viewBox="0 0 8 7"><path d="M0 0h8v5H3L1 7V5H0z" fill="#888"/></svg>&nbsp; 12 Comments</span></div>
    <p>Lorem ipsum dolor sit amet, consectetur adipiscing elit, sed do eiusmod tempor incididunt ut labore et dolore magna aliqua. Ut enim ad minim veniam, quis nostrud exercitation ullamco laboris nisi</p>
    <div class="read-more">Read more &#10140;</div>
  </div>
</article>

<article class="abs news-item" style="top:902px">
  <div class="news-thumb" role="img" aria-label="Photo of an older couple embracing outdoors" style="background:linear-gradient(120deg,#6e9a3c,#d8cdbd 50%,#9bb860)"></div>
  <div class="news-body">
    <h3>Nemo enim ipsam voluptatem</h3>
    <div class="meta"><span class="stars">★★★<span class="off">★★</span></span>
      <span><svg width="7" height="7" viewBox="0 0 8 8"><rect x="0" y="1" width="8" height="7" fill="#888"/></svg>&nbsp; April 3 , 2016</span>
      <span><svg width="8" height="7" viewBox="0 0 8 7"><path d="M0 0h8v5H3L1 7V5H0z" fill="#888"/></svg>&nbsp; 12 Comments</span></div>
    <p>Lorem ipsum dolor sit amet, consectetur adipiscing elit, sed do eiusmod tempor incididunt ut labore et dolore magna aliqua. Ut enim ad minim veniam, quis nostrud exercitation ullamco laboris nisi</p>
    <div class="read-more">Read more &#10140;</div>
  </div>
</article>

<aside class="abs message-box">
  <h3>LEAVE A MESSAGE</h3>
  <p>Lorem ipsum dolor sit amet, consectetur<br>adipiscing elit, sed do eiusmod</p>
  <div class="subscribe"><div class="field">Enter Your Email</div><div class="go">GO</div></div>
</aside>

<h2 class="abs section testi-title">Testimonials</h2>
<div class="abs quote-card">
  <span class="mark">&ldquo;&ldquo;</span>
  <div class="text">Lorem ipsum dolor sit amet, consectetur adipiscing elit, sed do eiusmod tempor incididunt ut labore et dolore magna aliqua. Ut enim ad minim veniam, quis nostrud exercitation Lorem ipsum dolor sit amet,</div>
</div>
<svg class="abs quote-tail" width="20" height="12" viewBox="0 0 20 12"><path d="M0 0h20L3 11z" fill="#fff" stroke="#e8e8e8"/><path d="M1 0h18" stroke="#fff" stroke-width="2"/></svg>
<div class="abs author-photo" role="img" aria-label="Portrait photo of the testimonial author"></div>
<div class="abs author-name"><span>John Doe</span> - &nbsp;Halden Memorial</div>
<div class="abs author-rule"></div>
<div class="abs pager">
  <span><svg width="5" height="7" viewBox="0 0 5 7"><path d="M4 .5 1 3.5l3 3" stroke="#333" fill="none"/></svg></span>
  <span><svg width="5" height="7" viewBox="0 0 5 7"><path d="M1 .5l3 3-3 3" stroke="#333" fill="none"/></svg></span>
</div>

<div class="abs side-rule"></div>
<h2 class="abs section gallery-title">Gallery</h2>
<div class="abs tile" style="left:532px;top:845px;background:linear-gradient(#4f7a5a,#a9c3c6 60%,#7c7360)" role="img" aria-label="Photo of a person in a yoga pose beside a mountain lake"></div>
<div class="abs tile" style="left:636px;top:845px;background:linear-gradient(#7ea64a,#a7c455 50%,#a33b2e)" role="img" aria-label="Photo of a child on an adult's shoulders among green trees"></div>
<div class="abs tile" style="left:532px;top:933px;background:linear-gradient(120deg,#8bab6a,#d9ccbe 55%,#a7bd8a)" role="img" aria-label="Photo of a smiling older couple"></div>
<div class="abs tile" style="left:636px;top:933px;background:linear-gradient(#f0a030,#e8661c 60%,#b8350e)" role="img" aria-label="Photo of a silhouette with an umbrella against an orange sunset"></div>

<footer class="abs site-footer">
  <svg width="799" height="159" viewBox="0 0 799 159" style="position:absolute;left:0;top:0"><path d="M0 0 399.5 47 799 0V159H0z" fill="#333333"/></svg>
</footer>
<div class="abs socials"><span></span><span></span><span></span><span></span><span></span></div>
<div class="abs foot-nav">HOME<b>/</b>ABOUT US<b>/</b>GALLERY<b>/</b>TESTIMONIALS<b>/</b>CONTACT US</div>
<div class="abs copy">2016 © Copyrights Halden Memorial.All Rights Reserved</div>

</body>
</html>
```